Catering Company Needs a Web Page Design

I already have my logo, and so I'm moving onto the next phase.. the web page design. Platrix is a gourmet catering company based in orlando, fl, set to launch in 2015. I will have a store location to host cooking classes as well.... and will be uploading cooking demo videos to my website weekly. Id like a blog section, and about, a video section, contact form, Services, Menu Samples..... My logo and concept is modern, innovative, and fun! I am targeting middle class to upper middle class women, but i want the site to be super unique.

Industry/Entity Type

Catering

Requirements
Must have
• The front/main page must have the logo... and the lingo ledger's definition of "platrix". I like movement... maybe the top banner can move somehow.. Im not a web designer, so i wont really know until I start seeing some examples. For now I dont have photos of my own cooking, so if you could use stock photos of catering dishes.. I uploaded a transparent logo also, maybe that could be the top banner placed over a scene of expertly plated hordourves...

```html
<!DOCTYPE html>
<html lang="en">
<head>
<meta charset="utf-8">
<title>Platrix – Gourmet Catering &amp; Cooking Classes</title>
<link href="https://fonts.googleapis.com/css2?family=Arimo:ital,wght@0,400;0,700;1,400&display=swap" rel="stylesheet">
<style>
:root{
  --brown:#3d2b21;
  --ink:#4a3a30;
  --orange:#ff5a1a;
  --green-dark:#7aa36a;
  --green-light:#a8cb8c;
  --grey-box:#efefef;
  --footer:#232323;
  --muted:#8a8a8a;
  --white:#ffffff;
}
*{margin:0;padding:0;box-sizing:border-box}
html,body{width:816px;height:1200px;overflow:hidden;background:var(--white)}
body{position:relative;font-family:"Arimo",Arial,sans-serif;color:var(--ink)}
.abs{position:absolute}

.brand{left:0;width:816px;top:50px;text-align:center}
.brand-name{font-size:56px;font-weight:700;color:var(--brown);letter-spacing:-1px;line-height:56px}
.brand-tag{font-size:9.5px;color:#6a5a4f;margin-top:0;padding-left:70px}

.main-nav{left:80px;top:147px;width:663px;height:63px;background:var(--brown);border-bottom:3px solid var(--orange);display:flex;justify-content:center;align-items:center;gap:24px;padding-bottom:6px}
.main-nav a{color:#e9e2dc;text-decoration:none;font-size:14.5px}
.main-nav a.active{color:var(--orange)}

.hero{left:80px;top:210px;width:663px;height:265px;background:linear-gradient(100deg,#6b2a12 0%,#c8642a 35%,#d99a4f 55%,#e8e2da 80%,#9ab7c9 100%)}
.progress{left:80px;top:475px;width:663px;height:5px;background:#6d6d6d}
.progress span{position:absolute;left:436px;top:0;width:227px;height:5px;background:var(--orange)}

.tabs{left:80px;top:481px;width:663px;height:63px;display:flex}
.tab{height:63px;display:flex;align-items:center;justify-content:center;gap:16px;color:var(--white);font-weight:700;font-size:16.5px;line-height:17px}
.tab.dark{background:var(--green-dark)}
.tab.light{background:var(--green-light)}

.section-title{left:80px;font-size:17px;font-weight:700;color:var(--ink);padding-bottom:2px;border-bottom:2px solid var(--orange)}
.carousel-arrows{left:669px;top:559px;display:flex;gap:6px}
.carousel-item{width:138px;height:138px;border-radius:50%;top:595px}
.rule{left:110px;top:745px;width:603px;height:1px;background:#e4e4e4}

.about-box{left:80px;top:800px;width:581px;height:80px;background:var(--grey-box);border-radius:3px}
.about-box p{position:absolute;left:88px;top:20px;width:410px;font-style:italic;font-size:10.3px;line-height:15.5px;color:#555}
.about-box::after{content:"";position:absolute;left:290px;bottom:-7px;border:7px solid transparent;border-bottom:0;border-top-color:var(--grey-box)}

.site-footer{left:80px;top:934px;width:663px;height:243px;background:var(--footer);border-bottom:3px solid var(--orange)}
.footer-title{position:absolute;top:28px;color:var(--white);font-size:17px;font-weight:700}
.blog-list{position:absolute;left:17px;top:63px;list-style:none}
.blog-list li{position:relative;height:40px;padding-left:13px;color:#eee;font-size:6.5px;line-height:12px}
.blog-list svg{position:absolute;left:0;top:2px}
.field{position:absolute;left:269px;width:155px;background:var(--grey-box);font-size:9.5px;color:#555;padding:2px 3px}
.submit{position:absolute;left:360px;top:200px;width:66px;height:19px;border-radius:6px;background:var(--white);font-size:9.5px;color:#222;text-align:center;line-height:19px}
.menu-grid{position:absolute;left:486px;top:62px;display:grid;grid-template-columns:repeat(3,36px);gap:6px}
.menu-grid div{width:36px;height:36px;border-radius:3px}
.social{position:absolute;left:572px;top:210px;display:flex;gap:2px}
.social span{width:14px;height:14px}
.copyright{left:110px;top:1187px;font-size:7px;color:var(--muted)}
</style>
</head>
<body>

<header class="brand abs">
  <div class="brand-name">platrix</div>
  <div class="brand-tag">Gourmet Catering &amp; Cooking Classes</div>
</header>

<nav class="main-nav abs">
  <a class="active" href="#">Home</a>
  <a href="#">About Us</a>
  <a href="#">Services</a>
  <a href="#">Classes</a>
  <a href="#">Video</a>
  <a href="#">Blog</a>
  <a href="#">Contact Us</a>
</nav>

<div class="hero abs" role="img" aria-label="Plated hors d'oeuvres: shot glasses of gazpacho, crispy shrimp and canapés on white spoons"></div>
<div class="progress abs"><span></span></div>

<div class="tabs abs">
  <div class="tab dark" style="width:163px"><span>Catering<br>Services</span>
    <svg width="16" height="22" viewBox="0 0 16 22" fill="none" stroke="#fff" stroke-width="2"><path d="M3 2v7M1 2v5a2 2 0 0 0 4 0V2M3 9v12M12 2c-3 2-3 7 0 8v11"/></svg></div>
  <div class="tab light" style="width:163px"><span>Cooking<br>Classes</span>
    <svg width="16" height="22" viewBox="0 0 16 22" fill="#fff"><rect x="2" y="2" width="2" height="19"/><rect x="9" y="4" width="5" height="9" rx="1"/><rect x="10.5" y="12" width="2" height="9"/></svg></div>
  <div class="tab dark" style="width:163px"><span>Blog</span>
    <svg width="16" height="18" viewBox="0 0 16 18" fill="#fff"><path d="M2 6a4 4 0 0 1 6-4 4 4 0 0 1 6 4c0 2-2 3-2 3v4H4V9S2 8 2 6z"/><rect x="4" y="14" width="8" height="3"/></svg></div>
  <div class="tab light" style="width:174px"><span>Videos</span>
    <svg width="10" height="22" viewBox="0 0 10 22" fill="#fff"><path d="M1 12l8 4.5-8 4.5z"/></svg></div>
</div>

<h2 class="section-title abs" style="top:556px">Food Carousel</h2>
<div class="carousel-arrows abs">
  <svg width="19" height="19" viewBox="0 0 19 19" fill="none" stroke="#bbb"><circle cx="9.5" cy="9.5" r="8.8"/><path d="M11 6l-3.5 3.5L11 13"/></svg>
  <svg width="19" height="19" viewBox="0 0 19 19" fill="none" stroke="#bbb"><circle cx="9.5" cy="9.5" r="8.8"/><path d="M8 6l3.5 3.5L8 13"/></svg>
</div>
<div class="carousel-item abs" style="left:111px;background:radial-gradient(circle,#e8c9c4,#6b3a2a 70%,#eee)" role="img" aria-label="Layered berry and chocolate mousse cakes"></div>
<div class="carousel-item abs" style="left:260px;background:radial-gradient(circle,#f1e2a8,#c9b070 60%,#4a4a2a)" role="img" aria-label="Assorted lemon and berry tartlets"></div>
<div class="carousel-item abs" style="left:409px;background:radial-gradient(circle,#d9dba0,#9aa36a 55%,#3d3a2a)" role="img" aria-label="Slice of pistachio layer cake"></div>
<div class="carousel-item abs" style="left:558px;background:radial-gradient(circle,#e0c070,#5a3020 55%,#7bc24a)" role="img" aria-label="Chocolate-glazed layer cake with mint"></div>
<div class="rule abs"></div>

<h2 class="section-title abs" style="top:760px">About Platrix</h2>
<div class="about-box abs">
  <p>Udipiscing nunc et posuere malesuada, magna ipsum luctus sem, eu sodales urna lacus id erat. Mauris dignissim libero sed lorem vestibulum tempor. Cras id pellentesque felis. Mauris libero felis, gravida vulputate feugiat ut libero.</p>
</div>

<footer class="site-footer abs">
  <h3 class="footer-title" style="left:30px">RECENT BLOG</h3>
  <ul class="blog-list">
    <li><svg width="11" height="14" viewBox="0 0 11 14" fill="none" stroke="#fff" stroke-width="2"><path d="M2 1l7 6-7 6"/></svg>Lorem ipsum dolor sit amet, consectetuer adipiscing elit,<br>sed diam nonummy</li>
    <li><svg width="11" height="14" viewBox="0 0 11 14" fill="none" stroke="#fff" stroke-width="2"><path d="M2 1l7 6-7 6"/></svg>Lorem ipsum dolor sit amet, consectetuer adipiscing elit,<br>sed diam nonummy</li>
    <li><svg width="11" height="14" viewBox="0 0 11 14" fill="none" stroke="#fff" stroke-width="2"><path d="M2 1l7 6-7 6"/></svg>Lorem ipsum dolor sit amet, consectetuer adipiscing elit,<br>sed diam nonummy</li>
    <li><svg width="11" height="14" viewBox="0 0 11 14" fill="none" stroke="#fff" stroke-width="2"><path d="M2 1l7 6-7 6"/></svg>Lorem ipsum dolor sit amet, consectetuer adipiscing elit,<br>sed diam nonummy</li>
  </ul>

  <h3 class="footer-title" style="left:269px">CONTACT FORM</h3>
  <div class="field" style="top:62px;height:17px">Name</div>
  <div class="field" style="top:101px;height:18px">Email</div>
  <div class="field" style="top:142px;height:51px">Comment</div>
  <div class="submit">Submit</div>

  <h3 class="footer-title" style="left:485px">OUR MENU</h3>
  <div class="menu-grid" role="img" aria-label="Menu sample dishes">
    <div style="background:#c45a3a"></div><div style="background:#7aa34a"></div><div style="background:#b89a5a"></div>
    <div style="background:#d0602a"></div><div style="background:#c9a070"></div><div style="background:#e0d4c8"></div>
    <div style="background:#b0785a"></div><div style="background:#e8c850"></div><div style="background:#8a4a2a"></div>
  </div>
  <div class="social">
    <span style="background:#3b5998"></span><span style="background:#3fa9e0"></span><span style="background:#0e76a8"></span><span style="background:#e0308a"></span><span style="background:#ea4c89"></span>
  </div>
</footer>

<div class="copyright abs">©All Rights Reserved- Brightfold Studio</div>

</body>
</html>
```